Brightfold Partners Website

Brightfold Partners Advisory Services is a company which provides specialised advise in carbon markets, climate policy, landscapes, resilience and change. We are based in Australia but the majority of our business is global. Our clients range from governments to large corporates and not for profit organisations.
Our focus is on developing the capabilities of government officials, business decision makers and land managers so they can better navigate the complexity of climate change and sustainability.
We are looking for a website that is consistent with the high end professional services which we provide to serious players.
I have attached two versions of our logo. I have also attached the back of our business card so you can get a sense of what we hand to potential clients.

Target Market(s)

Professional individuals, decision makers, board members etc, government officials.

Industry/Entity Type

Government

Number of Pages Required

4 page

Font styles to use
Serif
Sans Serif

Requirements
Must have
• Please provide
• 1. Home page
• 2. Service page template
• 3. Contact page
• 4. Lead expert profile page

```html
<!DOCTYPE html>
<html lang="en">
<head>
<meta charset="utf-8">
<title>Brightfold Partners</title>
<link rel="stylesheet" href="https://fonts.googleapis.com/css2?family=Cinzel:wght@400;600&family=Oxygen:wght@400;700&display=swap">
<style>
:root{
  --ink:#2f2f2f;
  --muted:#8c8c8c;
  --rule:#d8d8d8;
  --panel:#ebebeb;
  --field:#f7f7f7;
  --footer-box:#3b3b3b;
  --footer-line:#555;
  --white:#ffffff;
  --serif:"Cinzel", Georgia, serif;
  --sans:"Oxygen", Arial, sans-serif;
}
*{box-sizing:border-box;margin:0;padding:0}
html,body{width:974px;height:1200px;overflow:hidden;background:var(--white)}
body{position:relative;font-family:var(--sans);color:var(--ink)}
.abs{position:absolute}

/* header */
.site-header{left:0;top:0;width:974px;height:100px;background:linear-gradient(#fdfdfd,#ececec);border-top:4px solid #9a9a9a}
.brand{left:107px;top:16px;display:flex;align-items:center;gap:14px}
.brand-dot{width:56px;height:56px;border-radius:50%;background:#8a8a8a}
.brand-name{font-family:var(--serif);font-weight:400;font-size:27px;line-height:31px;letter-spacing:2px;color:var(--ink)}
.callout{left:727px;top:16px;display:flex;gap:6px;align-items:center}
.callout small{display:block;font-size:12px;color:var(--ink)}
.callout strong{display:block;font-size:18px;font-weight:400;color:var(--ink);line-height:20px}
.main-nav{right:106px;top:73px;display:flex;font-size:13px;color:var(--muted)}
.main-nav a{color:inherit;text-decoration:none;padding:0 15px;border-left:1px solid #bbb;line-height:16px}
.main-nav a:first-child{border-left:0;color:var(--ink)}
.main-nav a:last-child{padding-right:0}

/* hero */
.hero{left:0;top:100px;width:974px;height:362px;background:linear-gradient(90deg,#6b6f72 0%,#dfe4e6 30%,#eef2f3 50%,#d9dee0 70%,#5f6467 100%)}
.hero-arrow{top:155px;width:30px;height:30px;border-radius:50%;background:rgba(20,20,20,.75)}
.hero-caption{left:0;bottom:0;width:974px;height:36px;background:rgba(30,30,30,.7);color:var(--white);font-size:21px;line-height:36px;padding-left:174px}

/* section headings */
.heading{font-family:var(--serif);font-size:20px;letter-spacing:1px;color:var(--ink);white-space:nowrap}
.heading span{color:var(--muted)}

/* about */
.about-title{left:0;width:974px;top:480px;display:flex;justify-content:center;align-items:center;gap:8px}
.about-title i{width:24px;height:24px;border-radius:50%;background:#9a9a9a}
.about-text{left:117px;top:518px;width:740px;font-size:10.2px;line-height:17px;text-align:center;color:var(--ink)}

/* services */
.services{left:0;top:606px;width:974px;height:218px;background:var(--panel)}
.services-title{left:0;top:18px;width:974px;text-align:center}
.service{top:58px;width:150px;text-align:center;font-size:11px;line-height:14px;color:var(--ink)}
.service svg{display:block;margin:0 auto 10px}

/* lower columns */
.column{top:852px}
.col-head{display:flex;align-items:center;gap:8px;font-size:17px;height:29px;padding-bottom:6px;border-bottom:2px solid var(--rule);position:relative}
.col-head::after{content:"";position:absolute;left:6px;bottom:-8px;border:6px solid transparent;border-top-color:var(--rule);border-bottom:0}
.news-item{border-bottom:1px dashed #ccc;padding:12px 0 8px;font-size:9.6px;line-height:14px}
.news-item:last-of-type{border-bottom:0}
.news-item b{display:block;font-size:11px;font-weight:400;color:var(--ink)}
.read-more{font-size:11px;color:var(--ink);text-align:right;display:block;text-decoration:none}
.quote{left:0;top:43px;width:228px;height:106px;background:#eeeeee;border-radius:6px;padding:12px 10px 0 16px;text-indent:20px;font-size:9.6px;line-height:16px}
.quote::before{content:"\201C";position:absolute;left:12px;top:2px;text-indent:0;font-family:Georgia,serif;font-size:36px;line-height:36px;color:#c7c7c7}
.avatar{left:16px;top:131px;width:54px;height:54px;border:3px solid var(--white);background:linear-gradient(#7f8a94,#3d4a57);box-shadow:0 0 0 1px #ccc}
.client-name{left:83px;top:161px;font-size:10.5px}
.field{left:0;width:229px;height:23px;border:2px solid #dcdcdc;background:var(--field);border-radius:3px;font-size:10px;color:#666;padding:4px 6px}
.submit{left:-1px;top:172px;width:55px;height:19px;background:#3a3a3a;color:var(--white);font-size:12px;font-weight:700;text-align:center;line-height:19px;border-radius:2px}

/* footer */
.site-footer{left:0;top:1075px;width:974px;height:125px;background:linear-gradient(#3a3a3a,#262626);border-top:3px solid #bcbcbc;color:#ddd}
.f-box{top:13px;height:63px;background:var(--footer-box);border:1px solid var(--footer-line);padding:4px 9px}
.f-box h4{font-size:12.5px;font-weight:700;color:var(--white);margin-bottom:6px}
.f-input{width:146px;height:22px;background:#5c5c5c;color:#e0e0e0;font-size:10px;line-height:22px;padding-left:6px}
.f-go{left:159px;top:29px;width:25px;height:22px;background:#5c5c5c}
.f-line{display:flex;align-items:center;gap:6px;font-size:9.5px;line-height:17px;color:#ddd;white-space:nowrap}
.social{display:flex;gap:10px}
.social i{width:20px;height:20px;background:#8a8a8a}
.f-brand{left:652px;top:17px;display:flex;align-items:center;gap:12px}
.f-brand i{width:48px;height:48px;border-radius:50%;background:#9a9a9a}
.f-brand span{font-family:var(--serif);font-size:22px;line-height:27px;letter-spacing:1.5px;color:var(--white)}
.f-links{left:106px;top:96px;font-size:10.5px;color:var(--white)}
.f-copy{right:106px;top:96px;font-size:10.5px;color:var(--white)}
</style>
</head>
<body>

<header class="site-header abs">
  <div class="brand abs"><i class="brand-dot"></i><div class="brand-name">BRIGHTFOLD<br>PARTNERS</div></div>
  <div class="callout abs">
    <svg width="26" height="26" viewBox="0 0 26 26"><circle cx="13" cy="13" r="12" fill="none" stroke="#777" stroke-width="1.5"/><path d="M9 7c-2 2 1 9 7 12l2-2-3-3-2 1c-1-1-2-3-2-4l1-2-3-2z" fill="#777"/></svg>
    <div><small>Call Us Today</small><strong>123 555 0190</strong></div>
  </div>
  <nav class="main-nav abs"><a href="#">HOME</a><a href="#">OUR SERVICES</a><a href="#">CONTACT US</a><a href="#">LEAD EXPERT PROFILE</a></nav>
</header>

<section class="hero abs" role="img" aria-label="Photo of a consultant presenting to a boardroom of professionals by large windows">
  <div class="hero-arrow abs" style="left:108px">
    <svg width="30" height="30"><path d="M17 9l-6 6 6 6" fill="none" stroke="#fff" stroke-width="1.5"/></svg>
  </div>
  <div class="hero-arrow abs" style="left:834px">
    <svg width="30" height="30"><path d="M13 9l6 6-6 6" fill="none" stroke="#fff" stroke-width="1.5"/></svg>
  </div>
  <div class="hero-caption abs">Lorem ipsum dolor sit amet, consectetuer adipiscing elit sed diam</div>
</section>

<section class="about">
  <h2 class="about-title heading abs"><i></i><span>ABOUT</span>BRIGHTFOLD PARTNERS</h2>
  <p class="about-text abs">Lorem ipsum dolor sit amet, consectetuer adipiscing elit,Sed diam nonummy nibh euismod tincidunt ut laoreet dolore magna aliquam erat volutpat. Ut wisi enim ad minim veniam, quis nostrud exerci tation ullamcorper suscipit lobortis nisl ut aliquip &nbsp;commodo consequat. Duis autem vel eum iriure dolor in hendrerit in vulputate velit esse molestie consequat, vel ill dolore eu feugiat nulla facilisis at vero eros et accumsan et iusto odio dignissim qui blandit praesent luptatumdeelenit augue duis dolore te feugait nulla facilisi.</p>
</section>

<section class="services abs">
  <h2 class="services-title heading abs"><span>OUR</span> SERVICES</h2>

  <div class="service abs" style="left:108px">
    <svg width="106" height="106" viewBox="0 0 106 106"><circle cx="53" cy="53" r="51" fill="#fff" stroke="#444" stroke-width="2.5"/><circle cx="44" cy="47" r="12" fill="#222"/><path d="M20 86c2-14 12-22 24-22s22 8 24 22z" fill="#222"/><path d="M60 26h18a9 9 0 0 1 0 18h-10l-6 5v-5a9 9 0 0 1-2-18z" fill="none" stroke="#222" stroke-width="2.5"/><path d="M70 31v1M70 34v7" stroke="#222" stroke-width="3"/></svg>
    Corporate Advisory on<br>Carbon Markets
  </div>

  <div class="service abs" style="left:252px">
    <svg width="106" height="106" viewBox="0 0 106 106"><circle cx="53" cy="53" r="51" fill="#fff" stroke="#444" stroke-width="2.5"/><circle cx="42" cy="58" r="14" fill="none" stroke="#222" stroke-width="9" stroke-dasharray="6 4"/><circle cx="42" cy="58" r="5" fill="#222"/><circle cx="68" cy="36" r="10" fill="none" stroke="#222" stroke-width="7" stroke-dasharray="5 3"/><circle cx="68" cy="36" r="3" fill="#222"/></svg>
    Project Mechanisms<br>(carbon credits &amp; offsets)
  </div>

  <div class="service abs" style="left:412px">
    <svg width="106" height="106" viewBox="0 0 106 106"><circle cx="53" cy="53" r="51" fill="#fff" stroke="#444" stroke-width="2.5"/><path d="M22 24v56h62" fill="none" stroke="#222" stroke-width="3"/><rect x="28" y="60" width="9" height="17" fill="#222"/><rect x="41" y="52" width="9" height="25" fill="#222"/><rect x="54" y="58" width="9" height="19" fill="#222"/><rect x="67" y="44" width="9" height="33" fill="#222"/><path d="M28 52l14-12 10 8 20-20" fill="none" stroke="#222" stroke-width="3"/><path d="M66 26h9v9" fill="none" stroke="#222" stroke-width="3"/></svg>
    Monitoring, Reporting<br>&amp; Verification
  </div>

  <div class="service abs" style="left:563px">
    <svg width="106" height="106" viewBox="0 0 106 106"><circle cx="53" cy="53" r="51" fill="#fff" stroke="#444" stroke-width="2.5"/><path d="M53 20l-33 14h66z" fill="#222"/><rect x="22" y="37" width="62" height="5" fill="#222"/><rect x="27" y="45" width="7" height="27" fill="#222"/><rect x="40" y="45" width="7" height="27" fill="#222"/><rect x="53" y="45" width="7" height="27" fill="#222"/><rect x="66" y="45" width="7" height="27" fill="#222"/><rect x="20" y="75" width="66" height="7" fill="#222"/></svg>
    Institutional<br>Arrangements
  </div>

  <div class="service abs" style="left:701px">
    <svg width="106" height="106" viewBox="0 0 106 106"><circle cx="53" cy="53" r="51" fill="#fff" stroke="#444" stroke-width="2.5"/><circle cx="40" cy="34" r="8" fill="#222"/><path d="M28 86V56a10 10 0 0 1 20 0l6 4 22-28" fill="none" stroke="#222" stroke-width="9" stroke-linejoin="round"/><path d="M76 32l12-14" stroke="#222" stroke-width="2.5"/><rect x="34" y="62" width="18" height="24" rx="2" fill="#222"/></svg>
    Training &amp;<br>Coaching
  </div>
</section>

<section class="column news abs" style="left:115px;width:229px">
  <h3 class="col-head heading">
    <svg width="18" height="16" viewBox="0 0 18 16"><path d="M1 5h4l8-4v14l-8-4H1z M4 11l2 5h2l-1-4" fill="#555"/></svg>
    <span>LATEST</span>NEWS
  </h3>
  <div class="news-item" style="margin-top:6px"><b>11/12/2013</b>Lorem ipsum dolor sit amet, cctetuer adipiscingin elit, sed diam nummy nibh eui smod tinciduntiot vulputate velit esse molestie</div>
  <div class="news-item"><b>11/4/2012</b>Lorem ipsum dolor sit amet, cctetuer adipiscingin elit, sed diam nummy nibh eui smod tinciduntiot vulputate velit esse molestie</div>
  <a class="read-more" href="#" style="margin-top:4px">Read more &raquo;</a>
</section>

<section class="column testimonial abs" style="left:372px;width:232px;height:200px">
  <h3 class="col-head heading">
    <svg width="19" height="17" viewBox="0 0 19 17"><path d="M1 1h11v7H6l-3 3V8H1z" fill="#555"/><path d="M14 5h4v7h-2v3l-3-3H8V10h6z" fill="#555"/></svg>
    <span>CLIENT</span>TESTIMONIAL
  </h3>
  <blockquote class="quote abs">Duis autem vel eum iriureol hder in vultat velit esse moles conqat vela ilu dolor feugiat.Duis autem vel eum ure hendrern vultat velit esse autm vel eum iriure dol</blockquote>
  <div class="avatar abs" role="img" aria-label="Client portrait photo"></div>
  <div class="client-name abs">Mr. Dolore Eu Feugiat</div>
  <a class="read-more abs" href="#" style="left:172px;top:183px">Read more &raquo;</a>
</section>

<section class="column quick-contact abs" style="left:631px;width:229px;height:200px">
  <h3 class="col-head heading">
    <svg width="17" height="17" viewBox="0 0 17 17"><rect x="1" y="3" width="11" height="13" fill="none" stroke="#555" stroke-width="2"/><path d="M8 10l7-7 2 2-7 7H8z" fill="#555"/></svg>
    <span>QUICK</span>CONTACT
  </h3>
  <div class="field abs" style="top:43px">Name</div>
  <div class="field abs" style="top:72px">Email</div>
  <div class="field abs" style="top:101px;height:59px">Message</div>
  <div class="submit abs">Submit</div>
</section>

<footer class="site-footer abs">
  <div class="f-box abs" style="left:105px;width:199px">
    <h4>Subscribe to Newsletter</h4>
    <div class="f-input">Email here</div>
    <div class="f-go abs"><svg width="25" height="22"><path d="M11 7l4 4-4 4" fill="none" stroke="#fff" stroke-width="2.5"/></svg></div>
  </div>
  <div class="f-box abs" style="left:345px;width:126px">
    <h4>Contact Us</h4>
    <div class="f-line"><svg width="9" height="9" viewBox="0 0 9 9"><path d="M2 0c-2 2 1 7 6 9l1-2-2-2-1 1C5 5 4 4 4 3l1-1z" fill="#888"/></svg>012-555-0147</div>
    <div class="f-line"><svg width="10" height="8" viewBox="0 0 10 8"><rect width="10" height="8" fill="#888"/><path d="M0 0l5 4 5-4" fill="none" stroke="#3b3b3b"/></svg>info@ brightfold.com</div>
  </div>
  <div class="f-box abs" style="left:510px;width:96px">
    <h4>Follow Us</h4>
    <div class="social"><i></i><i></i><i></i></div>
  </div>
  <div class="f-brand abs"><i></i><span>BRIGHTFOLD<br>PARTNERS</span></div>
  <div class="f-links abs">Home &nbsp;| &nbsp;Our Services | &nbsp;Contact Us &nbsp;| &nbsp;Lead Export Profile</div>
  <div class="f-copy abs">Copyright &copy; 2014 Brightfold Partners. All Rights Reserved</div>
</footer>

</body>
</html>
```